Real Estate Templates in Canva

I need someone to create a robust set of Canva template designs for my real estate company team, to streamline content. I need a catalog for my agents to easily go in and pick from different designs and customize for themselves. The correct candidate can emulate the style found on these sites., and in the attached images. I have also uploaded logos to be used.(https://www.tundrahomesgroup.com/) and (https://meetcalverly.com/)

I want a fantastic sharp style that has great color blend and is attractive and matches my brand well.

The correct candidate will have access to my Canva Brand Kit and build templates inside of my account.

Also attached is a screenshot of my main color codes

The types of templates can include, but not be limited to the following:
BOTH DIGITAL FOR SOCIAL MEDIA AND PRINT VERSIONS
Listings flyers
Clients testimonials
market stats
open houses
Realtor Insights
Realtor analysis
sold properties
new listing properties
under contract properties
coming soon properties
Bullet points summarizing key data
Photo of the client at closing
Photo of the client at their home

Property Listing Template:

Description of the property
High-quality images
Key features and amenities
Open House Invitation:

Date, time, and location details
Compelling visuals of the property
Call-to-action for attendance
Just Sold Announcement:

Property details (address, price, etc.)
Celebratory message
Testimonials from satisfied clients
Testimonial Template:

Client testimonial
Photo of the client (with permission)
Brief background or story
Market Update Infographic:

Visual representation of current market trends
Realtor's insights and analysis
Buyer's Guide:

Step-by-step guide for homebuyers
Infographics explaining the buying process
Tips and advice for a successful purchase
Seller's Guide:

Information on preparing a home for sale
Infographics on the selling process
Tips for maximizing property value
Seasonal Greetings Template:

Personalized message for clients
Festive visuals or themes
Wishes for a successful year ahead
Neighborhood Highlight:

Showcase a specific neighborhood
Key attractions, schools, amenities
Testimonials from residents (if available)
Behind-the-Scenes:

Photos or videos of the realtor at work
Personalized messages about the real estate process
Humanizing content to connect with the audience
Infographic: Benefits of Working with a Realtor:

Visual representation of the advantages
Statistics or data supporting the benefits
Clear, concise points for easy consumption
Interactive Polls or Quizzes:

Engage the audience with fun polls
Real estate-related quizzes
Encourage interaction and sharing
Client Appreciation Post:

Thanking clients for their trust
Sharing success stories
Expressing gratitude with visuals
Video Tour Teaser:

Sneak peek of a property tour
Create excitement and anticipation

Target Market(s)

General Population ages 30-70

Requirements
Must have
• 60 plus designs
Nice to have
• 100 plus designs

```html
<!DOCTYPE html>
<html lang="en">
<head>
<meta charset="utf-8">
<title>Tundra Homes Group – Featured Listings Flyer Set</title>
<link rel="stylesheet" href="https://fonts.googleapis.com/css2?family=Bebas+Neue&family=Jost:wght@300;400;600&display=swap">
<style>
  :root {
    --brand-orange: #f39433;
    --brand-orange-soft: #f6b26a;
    --ink: #1c1c1c;
    --paper: #ffffff;
    --backdrop: #efefef;
  }
  * { box-sizing: border-box; margin: 0; padding: 0; }
  html, body { width: 759px; height: 1200px; overflow: hidden; background: var(--backdrop); }
  .stage {
    position: relative; width: 960px; height: 1518px;
    transform: scale(0.790625); transform-origin: 0 0;
    font-family: "Jost", sans-serif; color: var(--ink);
  }
  .page {
    position: absolute; left: 233px; width: 497px; height: 702px;
    background: var(--paper); overflow: hidden;
    box-shadow: 0 4px 14px rgba(0,0,0,0.18);
  }
  .page--cover { top: 38px; }
  .page--listing { top: 766px; }
  .shape { position: absolute; display: block; }

  .brand { position: absolute; display: flex; align-items: center; gap: 8px; }
  .brand__dot { width: 40px; height: 40px; border-radius: 50%; background: var(--brand-orange); flex: none; }
  .brand__name { font-family: "Jost", sans-serif; font-weight: 600; font-size: 18px; color: var(--brand-orange); line-height: 1.05; width: 110px; }
  .page--cover .brand { left: 307px; top: 38px; }
  .page--listing .brand { left: 43px; top: 36px; }

  .cover__title {
    position: absolute; left: 42px; top: 100px;
    font-family: "Bebas Neue", sans-serif; font-size: 49px; line-height: 46px;
    color: var(--paper); letter-spacing: 0.5px;
  }
  .topic-list {
    position: absolute; right: 33px; top: 110px; list-style: none;
    text-align: right; font-size: 14.5px; font-weight: 300; line-height: 20.8px;
  }
  .cover__photo {
    position: absolute; left: 0; top: 385px; width: 497px; height: 496px; border-radius: 50%;
    background: linear-gradient(180deg, #6f6656 0%, #8a7a5c 45%, #c8944a 70%, #e0963c 100%);
  }
  .web-link { position: absolute; font-size: 17px; font-weight: 400; }
  .page--cover .web-link { left: 42px; top: 653px; color: var(--paper); font-size: 18px; }
  .page--listing .web-link { right: 33px; top: 656px; font-size: 14.5px; }

  .listing__intro { position: absolute; left: 42px; top: 107px; font-size: 14.5px; line-height: 20.8px; font-weight: 300; }
  .listing__intro strong { font-weight: 600; }
  .photo { position: absolute; width: 201px; }
  .photo--a { left: 42px; top: 196px; height: 150px; background: linear-gradient(180deg, #9fc2e4 0%, #5a6b84 30%, #3e4d2f 50%, #a59a7c 75%, #6b5a45 100%); }
  .photo--b { left: 256px; top: 196px; height: 150px; background: linear-gradient(180deg, #a9c4dd 0%, #4b5a3a 40%, #857a5e 75%, #3d3425 100%); }
  .photo--c { left: 42px; top: 359px; height: 133px; background: linear-gradient(180deg, #4f7fc4 0%, #e9eef2 35%, #5d7a55 60%, #6f9b3e 100%); }
  .photo--d { left: 256px; top: 359px; height: 133px; background: linear-gradient(180deg, #6a8fbf 0%, #7a5a3a 40%, #8e6b44 60%, #6e9a3c 100%); }
  .photo--e { left: 42px; top: 506px; height: 134px; background: linear-gradient(180deg, #7f8aa4 0%, #d59a70 35%, #4b4646 55%, #dfe3ea 75%, #c9cfd8 100%); }
</style>
</head>
<body>
<main class="stage">

  <section class="page page--cover">
    <svg class="shape" width="497" height="340" viewBox="0 0 497 340" aria-hidden="true">
      <path d="M0 0 H350 C285 10 252 55 240 140 C228 228 205 262 18 325 L0 300 Z" fill="var(--brand-orange)"/>
    </svg>
    <div class="brand"><span class="brand__dot"></span><span class="brand__name">Tundra Homes Group</span></div>
    <h1 class="cover__title">Our<br>Featured<br>Listings</h1>
    <ul class="topic-list">
      <li>Clients testimonials</li>
      <li>Market stats</li>
      <li>Open houses</li>
      <li>Realtor Insights</li>
      <li>Realtor analysis</li>
      <li>Dold properties</li>
      <li>New listing properties</li>
      <li>Under contract properties</li>
      <li>Coming soon properties</li>
      <li>Bullet points summarizing key data</li>
      <li>Photo of the client at closing</li>
      <li>Photo of the client at their home</li>
    </ul>
    <div class="cover__photo" role="img" aria-label="Aerial photo of open prairie land with a highway and pine trees, tinted orange at the bottom"></div>
    <p class="web-link">www.tundrahomesgroup.com</p>
  </section>

  <section class="page page--listing">
    <svg class="shape" style="left:260px;top:0" width="237" height="185" viewBox="0 0 237 185" aria-hidden="true">
      <path d="M135 0 H237 V160 C190 185 120 182 60 165 C20 155 0 145 5 130 C20 90 40 50 75 35 C105 22 120 10 135 0 Z" fill="var(--brand-orange)"/>
    </svg>
    <div class="brand"><span class="brand__dot"></span><span class="brand__name">Tundra Homes Group</span></div>
    <p class="listing__intro">
      <strong>Property Listing Template:</strong><br>
      Description of the property<br>
      High-quality images<br>
      Key features and amenities
    </p>
    <div class="photo photo--a" role="img" aria-label="Mountain range above a forested valley with a small cabin"></div>
    <div class="photo photo--b" role="img" aria-label="Tall pine trees along a rural road"></div>
    <div class="photo photo--c" role="img" aria-label="Green meadow below rugged mountains and cloudy sky"></div>
    <div class="photo photo--d" role="img" aria-label="Log home with porch and garden beside a large tree"></div>
    <div class="photo photo--e" role="img" aria-label="Log house in snow at sunset"></div>
    <svg class="shape" style="left:180px;top:470px" width="317" height="232" viewBox="0 0 317 232" aria-hidden="true">
      <path d="M60 232 C40 170 45 100 90 55 C140 10 230 -5 317 20 V232 Z" fill="var(--brand-orange-soft)" opacity="0.9"/>
    </svg>
    <p class="web-link">www.tundrahomesgroup.com</p>
  </section>

</main>
</body>
</html>
```